Powerpoint visual improvements

I need a cover page, and our beliefs page and differentiating factors page / graphic design for our presentation. For the cover page I would just like an attractive design that incorporate our architectural concept with columns and potentially our logo. For the beliefs page I just want a more attractive presentatoin of the concepts. For the differentiating factors page I want a graphic that captures the points about how we are different from competitors. I have used the attached content to date, but I think it can be improved. The text is included in the graphic and I would also like to make sure the firm logo is incorporated.

Target Market(s)

Individual and institutional investors.

Industry/Entity Type

Investment Advisory

Requirements
Must have
• Our corporate colors are generally RGB 145,148,149; 66,68,76; 0,0,153; and 0,63,127. Our logo is attached. Our primary font is Georgia. Our website is www.PelmarCW.com. The key pages are www.PelmarCW.com/beliefs and www.PelmarCW.com/value we are trying to capture in a presentation. We also need a new presentation cover. Use the website as a reference for the type of imagery we like.

```html
<!DOCTYPE html>
<html lang="en">
<head>
<meta charset="utf-8">
<title>Pelmar Capital Wealth — Presentation Slides</title>
<link href="https://fonts.googleapis.com/css2?family=Bebas+Neue&family=Gelasio:wght@400;700&display=swap" rel="stylesheet">
<style>
  :root {
    --navy: #1f3c84;
    --corp-blue: #003f7f;
    --gray: #7d8081;
    --gray-light: #a3a5a6;
    --ink: #42444c;
    --white: #ffffff;
    --page: #ffffff;
  }
  * { box-sizing: border-box; margin: 0; padding: 0; }
  html, body { width: 1000px; height: 1200px; overflow: hidden; background: var(--page); }
  body { position: relative; font-family: "Gelasio", Georgia, serif; color: var(--ink); }

  .slide {
    position: absolute; width: 460px; height: 259px; overflow: hidden;
    background: var(--white);
    box-shadow: 2px 3px 6px rgba(0,0,0,.35);
  }
  .col-a { left: 30px; } .col-b { left: 511px; }
  .row-1 { top: 26px; } .row-2 { top: 314px; } .row-3 { top: 601px; } .row-4 { top: 887px; }

  .abs { position: absolute; }
  .center { left: 0; right: 0; text-align: center; }
  .headline { font-family: "Bebas Neue", "Arial Narrow", sans-serif; font-weight: 400; letter-spacing: .2px; line-height: 1; }
  .body-copy { font-size: 5.6px; line-height: 1.35; color: var(--gray); }
  .meta { font-size: 4.2px; letter-spacing: .4px; color: var(--gray); text-transform: uppercase; }

  /* photo stand-ins */
  .photo { position: absolute; }
  .photo-columns-band { left: 0; right: 0; bottom: 0; height: 42px;
    background: linear-gradient(90deg, #5e5f60 0%, #c9c9c8 18%, #8a8a8a 35%, #d5d4d2 52%, #4a4a4b 68%, #bdbcba 85%, #8f8f8f 100%); }
  .photo-colonnade { inset: 0;
    background: linear-gradient(180deg, #3e4b5c 0%, #8c98a6 35%, #b7b3a6 65%, #3d3a36 100%); }
  .photo-tower-dark { inset: 0;
    background: linear-gradient(125deg, #3f3b33 0%, #6d6557 40%, #8b8678 60%, #4e5158 100%); }
  .photo-tower-blue { inset: 0;
    background: linear-gradient(125deg, #1d3b73 0%, #2c5296 50%, #234a8a 100%); }
  .photo-pillars { left: 0; top: 0; bottom: 0; width: 176px;
    background: linear-gradient(100deg, #7a5a2e 0%, #c9c2b4 35%, #e6e3dc 55%, #8d877c 80%, #5e5a52 100%); }
  .photo-map { left: 175px; top: 0; right: 0; bottom: 0;
    background: linear-gradient(135deg, #e4e4e4 0%, #cfcfcf 45%, #dedede 100%); }

  /* brand stand-in */
  .brand-mark { display: flex; align-items: center; justify-content: center; gap: 6px; }
  .brand-dot { border-radius: 50%; display: inline-block; }
  .brand-name { font-family: "Gelasio", Georgia, serif; font-weight: 700; letter-spacing: 1px; }

  .overlay-panel { position: absolute; left: 83px; top: 82px; width: 291px; height: 123px; background: rgba(255,255,255,.72); }

  .footer-line { position: absolute; bottom: 8px; font-size: 4.2px; letter-spacing: .3px; color: var(--gray); text-transform: uppercase; }

  .diagram { position: absolute; left: 0; top: 0; width: 460px; height: 259px; }
  .node-title { font-family: "Bebas Neue", "Arial Narrow", sans-serif; font-size: 10px; color: var(--navy); }
  .node-copy { font-size: 3.8px; line-height: 1.3; color: var(--gray); }
  .point-label { position: absolute; font-size: 5.6px; line-height: 1.3; letter-spacing: .4px; color: var(--gray); text-transform: uppercase; }

  .contact { font-size: 5px; line-height: 1.5; color: var(--gray); }
  .firm-name { font-family: "Gelasio", Georgia, serif; font-weight: 700; font-size: 15px; color: var(--navy); letter-spacing: .5px; }
  .firm-sub { font-size: 7.5px; color: var(--navy); letter-spacing: .3px; text-transform: uppercase; }
  .social { position: absolute; width: 26px; height: 26px; border-radius: 50%; border: 1.6px solid var(--gray-light); background: var(--white); }
</style>
</head>
<body>

<!-- Cover, light -->
<section class="slide col-a row-1" aria-label="Cover slide, light">
  <h1 class="abs center headline" style="top:54px;font-size:26px;color:var(--gray);">Presentation Title</h1>
  <p class="abs center body-copy" style="top:80px;">Lorem ipsum dolor sit amet, consetetur sadipscing elitr,<br>sed diam nonumy eirmod tempor invidunt ut labore et<br>dolore magna.</p>
  <div class="abs center brand-mark" style="top:146px;">
    <span class="brand-dot" style="width:20px;height:20px;background:var(--gray);"></span>
    <span class="brand-name" style="font-size:20px;color:var(--gray);">PELMAR</span>
  </div>
  <p class="abs center meta" style="top:201px;">Date &nbsp;|&nbsp; Placeholder Text</p>
  <div class="photo photo-columns-band" role="img" aria-label="Black and white close-up of stone columns"></div>
</section>

<!-- Cover, colonnade -->
<section class="slide col-b row-1" aria-label="Cover slide, colonnade">
  <div class="photo photo-colonnade" role="img" aria-label="Classical colonnade with tall stone columns under a blue sky"></div>
  <div class="overlay-panel"></div>
  <h1 class="abs center headline" style="top:97px;font-size:25px;color:var(--navy);">Presentation Title</h1>
  <p class="abs center body-copy" style="top:125px;">Lorem ipsum dolor sit amet, consetetur sadipscing elitr, sed diam nonumy<br>eirmod tempor invidunt ut labore et dolore magna.</p>
  <div class="abs center brand-mark" style="top:158px;">
    <span class="brand-dot" style="width:12px;height:12px;background:var(--navy);"></span>
    <span class="brand-name" style="font-size:12px;color:var(--navy);">PELMAR</span>
  </div>
  <p class="abs center meta" style="top:191px;">Date &nbsp;|&nbsp; Placeholder Text</p>
</section>

<!-- Section divider, dark -->
<section class="slide col-a row-2" aria-label="Section slide, dark">
  <div class="photo photo-tower-dark" role="img" aria-label="Upward view of a stone tower with columns, darkened"></div>
  <div class="abs center brand-mark" style="top:66px;">
    <span class="brand-dot" style="width:22px;height:22px;background:var(--white);"></span>
    <span class="brand-name" style="font-size:22px;color:var(--white);">PELMAR</span>
  </div>
  <h2 class="abs center headline" style="top:133px;font-size:24px;color:var(--white);">Lorem Ipsum Dolor</h2>
  <p class="abs center body-copy" style="top:160px;color:#e6e6e6;">Lorem ipsum dolor sit amet, consetetur sadipscing elitr, sed diam<br>nonumy eirmod tempor invidunt ut labore et dolore magna.</p>
  <p class="abs center meta" style="top:238px;color:#d8d8d8;">Date &nbsp;|&nbsp; Placeholder Text</p>
</section>

<!-- Section divider, blue -->
<section class="slide col-b row-2" aria-label="Section slide, blue">
  <div class="photo photo-tower-blue" role="img" aria-label="Upward view of a stone tower with columns under a blue tint"></div>
  <div class="abs center brand-mark" style="top:113px;">
    <span class="brand-dot" style="width:32px;height:32px;background:#d9dde4;"></span>
    <span class="brand-name" style="font-size:30px;color:#d9dde4;">PELMAR</span>
  </div>
</section>

<!-- Our Beliefs -->
<section class="slide col-a row-3" aria-label="Our beliefs slide">
  <div class="photo photo-pillars" role="img" aria-label="Tall white columns in front of a stone building at sunset"></div>
  <h2 class="abs headline" style="left:176px;right:0;text-align:center;top:14px;font-size:15px;color:var(--navy);">Our Beliefs</h2>
  <p class="abs body-copy" style="left:190px;right:14px;text-align:center;top:33px;">Lorem Ipsum has been the industry's standard dummy text ever since the 1500s, when an unknown printer took a galley of type and scrambled it to make a type specimen.</p>

  <svg class="diagram" viewBox="0 0 460 259" aria-hidden="true">
    <g fill="none" stroke="var(--navy)" stroke-width="1.1">
      <!-- left bracket -->
      <path d="M246 134 H256 M251 134 V160 M246 160 H256 M251 140 H286 M251 154 H286"/>
      <!-- right bracket -->
      <path d="M370 134 H360 M365 134 V160 M370 160 H360 M365 140 H330 M365 154 H330"/>
      <!-- coin icon -->
      <ellipse cx="243" cy="83" rx="6" ry="4.5"/>
      <path d="M240 88 V90 M246 88 V90"/>
      <!-- magnifier icon -->
      <circle cx="370" cy="82" r="4.5"/>
      <path d="M373.5 85.5 L377.5 89.5"/>
      <!-- target icon -->
      <circle cx="243" cy="218" r="5.5"/><circle cx="243" cy="218" r="3"/>
      <path d="M240 209 V212 M243 208 V211 M246 209 V212"/>
      <!-- pointer icon -->
      <path d="M368 212 L368 223 L371 220 L374 225 L376 224 L373 219 L377 219 Z"/>
    </g>
    <circle cx="308" cy="147" r="17" fill="var(--navy)"/>
    <text x="308" y="149" text-anchor="middle" font-family="Gelasio, Georgia, serif" font-weight="700" font-size="6" fill="#fff" letter-spacing=".4">PELMAR</text>
  </svg>

  <div class="abs" style="left:212px;top:97px;width:60px;text-align:center;">
    <div class="node-title">Cost Matters</div>
    <p class="node-copy">Aenean commodo ligula eget dolor. Aenean massa. Cum sociis natoque penatibus.</p>
  </div>
  <div class="abs" style="left:340px;top:97px;width:60px;text-align:center;">
    <div class="node-title">Research Matters</div>
    <p class="node-copy">Aenean commodo ligula eget dolor. Aenean massa. Cum sociis natoque penatibus.</p>
  </div>
  <div class="abs" style="left:212px;top:172px;width:60px;text-align:center;">
    <div class="node-title">Focus Matters</div>
    <p class="node-copy">Aenean commodo ligula eget dolor. Aenean massa. Cum sociis natoque penatibus.</p>
  </div>
  <div class="abs" style="left:340px;top:172px;width:60px;text-align:center;">
    <div class="node-title">Access Matters</div>
    <p class="node-copy">Aenean commodo ligula eget dolor. Aenean massa. Cum sociis natoque penatibus.</p>
  </div>

  <p class="footer-line" style="left:186px;">Pelmar &nbsp;|&nbsp; Capital Wealth</p>
  <p class="footer-line" style="left:434px;">5</p>
</section>

<!-- The Pelmar Difference -->
<section class="slide col-b row-3" aria-label="The Pelmar difference slide">
  <h2 class="abs headline" style="left:28px;top:22px;font-size:24px;line-height:1.3;color:var(--navy);text-align:center;width:100px;">The Pelmar<br>Difference</h2>
  <div class="abs body-copy" style="left:138px;top:20px;width:262px;font-size:5.2px;">
    <p>Lorem ipsum dolor sit amet, consectetuer adipiscing elit. Aenean commodo ligula eget dolor. Aenean massa. Cum sociis natoque penatibus et magnis dis parturient montes, nascetur ridiculus mus. Donec quam felis, ultricies nec, pellentesque eu, pretium quis, sem. Nulla consequat massa quis enim. Donec pede justo, fringilla vel, aliquet nec, vulputate eget, arcu.</p>
    <p style="margin-top:4px;">In enim justo, rhoncus ut, imperdiet a, venenatis vitae, justo. Nullam dictum felis eu pede mollis pretium. Integer tincidunt. Cras dapibus. Vivamus elementum semper nisi. Aenean vulputate eleifend tellus. Aenean leo ligula, porttitor eu, consequat vitae, eleifend ac, enim.</p>
  </div>

  <svg class="diagram" viewBox="0 0 460 259" aria-hidden="true">
    <g fill="none" stroke="var(--navy)" stroke-width="1.1">
      <path d="M130 162 V170 M130 166 H209"/>
      <path d="M329 162 V170 M329 166 H249"/>
      <path d="M170 140 V151 H210"/>
      <path d="M170 192 V181 H210"/>
      <path d="M288 140 V151 H248"/>
      <path d="M288 192 V181 H248"/>
    </g>
    <circle cx="229" cy="166" r="18" fill="var(--navy)"/>
    <text x="229" y="168" text-anchor="middle" font-family="Gelasio, Georgia, serif" font-weight="700" font-size="6.2" fill="#fff" letter-spacing=".4">PELMAR</text>
  </svg>

  <p class="point-label" style="left:140px;top:118px;width:60px;text-align:center;">Transparent Communication</p>
  <p class="point-label" style="left:257px;top:118px;width:60px;text-align:center;">Experienced Investors</p>
  <p class="point-label" style="left:58px;top:155px;width:62px;text-align:right;">Institutional Research Process</p>
  <p class="point-label" style="left:338px;top:155px;width:70px;">Independent Portfolio Construction</p>
  <p class="point-label" style="left:140px;top:204px;width:60px;text-align:center;">Proactive Total Fee Management</p>
  <p class="point-label" style="left:257px;top:204px;width:60px;text-align:center;">Sound Operational Platform</p>

  <p class="footer-line" style="left:22px;">Pelmar &nbsp;|&nbsp; Capital Wealth</p>
  <p class="footer-line" style="left:434px;">6</p>
</section>

<!-- Closing, light -->
<section class="slide col-a row-4" aria-label="Closing contact slide">
  <div class="abs brand-mark" style="left:56px;top:94px;">
    <span class="brand-dot" style="width:24px;height:24px;background:var(--gray);"></span>
    <span class="brand-name" style="font-size:22px;color:var(--gray);">PELMAR</span>
  </div>
  <div class="abs" style="right:48px;top:64px;text-align:right;">
    <div class="firm-name">PELMAR</div>
    <div class="firm-sub">Capital Wealth</div>
    <p class="contact" style="margin-top:10px;">418 W Harbor Pkwy, Suite 310<br>Lakeview, WI 53120</p>
    <p class="contact" style="margin-top:3px;">Phone: &nbsp;1-800-555-0142<br>Email: &nbsp;info@pelmarcw.com</p>
  </div>
  <span class="social" style="left:310px;top:174px;" aria-label="Social profile"></span>
  <span class="social" style="left:345px;top:174px;" aria-label="Social profile"></span>
  <span class="social" style="left:381px;top:174px;" aria-label="Social profile"></span>
  <div class="photo photo-columns-band" role="img" aria-label="Black and white close-up of stone columns"></div>
</section>

<!-- Closing, map -->
<section class="slide col-b row-4" aria-label="Closing slide with office location">
  <div class="abs brand-mark" style="left:0;width:175px;top:38px;">
    <span class="brand-dot" style="width:20px;height:20px;background:var(--navy);"></span>
  </div>
  <div class="abs" style="left:0;width:175px;top:100px;text-align:center;">
    <div class="firm-name">PELMAR</div>
    <div class="firm-sub">Capital Wealth</div>
    <p class="contact" style="margin-top:10px;">418 W Harbor Pkwy, Suite 310<br>Lakeview, WI 53120</p>
    <p class="contact" style="margin-top:3px;">Phone: &nbsp;1-800-555-0142<br>Email: &nbsp;info@pelmarcw.com</p>
  </div>
  <span class="social" style="left:41px;top:208px;" aria-label="Social profile"></span>
  <span class="social" style="left:76px;top:208px;" aria-label="Social profile"></span>
  <span class="social" style="left:111px;top:208px;" aria-label="Social profile"></span>
  <div class="photo photo-map" role="img" aria-label="Grey road map of the Great Lakes region marking the office location"></div>
</section>

</body>
</html>
```